Business Card Design Project

I am looking for a business card design for our online furniture company. Our company name is Tavrolen Goods, LLC. We sell exquisitely crafted high-end furniture and accessories tailored for a customer base with a wide range of design tastes. We encourage our customers to be creative when decorating the space in which they live and we should have a business card that is representative of that philosophy. A whimsical design is not off limits, but it should not have a look that can be off-putting to male customers. Professional single men are in the market for our products as well as women; therefore, we want a card that is equally appealing to both sexes.

Our card should be as unique as it is creative and should stand apart from typical and often bland business cards. In others words we looking for a card design that will elicit an interaction from other people to help them remember who we are. When a member of our team hands a potential customer our card, we want that person to feel as if they are holding a piece of art. We would like the card to be worthy of conversation unto itself. The card should be visually stimulating in such a way that it will be difficult for recipients to discard, even if they have electronically stored our business information. Keep in mind we will also be giving potential suppliers and interior designers alike our card so it needs to demonstrate that we are a serious and credible business. Both sides of the card can be used for the design if necessary. It may be beneficial for you to consult our website for further inspiration. Please do not hesitate to contact me with any questions you may have over the course of this project.

Industry/Entity Type

Business

Requirements
Must have
• Mirek Dunsby
Tavrolen Goods, LLC
Owner/Founder
mdunsby@tavrolengoods.example
555-284-9173
Customize Your Lifestyle (company slogan, if needed)
www.tavrolengoods.example

```html
<!DOCTYPE html>
<html lang="en">
<head>
<meta charset="utf-8">
<title>Tavrolen Goods – Business Card</title>
<link rel="stylesheet" href="https://fonts.googleapis.com/css2?family=Archivo+Black&family=Crimson+Pro:ital,wght@0,400;0,600;1,700&display=swap">
<style>
  :root {
    --page: #ffffff;
    --ink-dark: #1c1c1c;
    --band-dark: #222222;
    --orange-light: #ffd447;
    --orange-mid: #fbb428;
    --orange-deep: #f0900c;
    --brand-orange: #f6ad3c;
    --slogan-yellow: #f4c544;
    --contact-band: rgba(255, 236, 178, 0.5);
    --text-brown: #3a2c1c;
    --upholstery-light: #c99a56;
    --upholstery-dark: #7a5526;
  }
  * { box-sizing: border-box; margin: 0; padding: 0; }
  html, body {
    width: 1200px; height: 399px; overflow: hidden;
    background: var(--page);
  }
  .sheet { position: relative; width: 1200px; height: 399px; }
  .card {
    position: absolute; top: 16px;
    width: 560px; height: 358px;
    border-radius: 12px; overflow: hidden;
    background: linear-gradient(180deg, var(--orange-light) 0%, var(--orange-mid) 55%, var(--orange-deep) 100%);
    box-shadow: 0 0 0 1px rgba(0,0,0,0.08);
  }
  .card--front { left: 14px; }
  .card--back { left: 628px; }
  .card__wave { position: absolute; inset: 0; width: 100%; height: 100%; }
  .brand {
    position: absolute; left: 12px; top: 8px;
    display: flex; align-items: center; gap: 10px;
  }
  .brand__mark {
    width: 32px; height: 32px; background: var(--brand-orange); border-radius: 4px;
  }
  .brand__name {
    font-family: "Archivo Black", sans-serif;
    font-size: 27px; color: var(--brand-orange); letter-spacing: 0.5px;
  }
  .slogan {
    position: absolute; left: 18px; top: 62px;
    font-family: "Crimson Pro", serif; font-weight: 600;
    font-size: 25px; letter-spacing: 1.5px; word-spacing: 5px;
    color: var(--slogan-yellow);
  }
  .person {
    position: absolute; right: 38px; top: 140px; text-align: right;
    font-family: "Crimson Pro", serif; color: var(--ink-dark);
  }
  .person__name { font-size: 34px; font-weight: 600; word-spacing: 6px; }
  .person__role {
    font-size: 21px; font-style: italic; font-weight: 700;
    border-bottom: 1px solid rgba(0,0,0,0.35); padding-bottom: 2px; display: inline-block;
  }
  .sofa-art {
    position: absolute; left: 22px; top: 212px; width: 225px; height: 112px;
    border-radius: 40px 40px 10px 10px;
    background: radial-gradient(ellipse at 50% 35%, var(--upholstery-light), var(--upholstery-dark));
    opacity: 0.85;
  }
  .footer-brand {
    position: absolute; right: 20px; bottom: 12px;
    display: flex; align-items: center; gap: 5px;
  }
  .footer-brand__mark { width: 16px; height: 16px; background: var(--ink-dark); }
  .footer-brand__name {
    font-family: "Crimson Pro", serif; font-weight: 600;
    font-size: 19px; color: var(--ink-dark); letter-spacing: 0.5px;
  }
  .contact-band {
    position: absolute; left: 0; right: 0; top: 194px; height: 124px;
    background: var(--contact-band);
  }
  .contact {
    position: absolute; left: 20px; top: 200px;
    font-family: "Crimson Pro", serif; font-weight: 600;
    font-size: 22px; color: var(--text-brown); line-height: 38px;
    list-style: none; letter-spacing: 0.5px;
  }
  .contact__label { margin-right: 10px; }
</style>
</head>
<body>
<main class="sheet">

  <section class="card card--front" aria-label="Card front">
    <svg class="card__wave" viewBox="0 0 560 358" aria-hidden="true">
      <path d="M0 0 H560 V66 C470 80 380 132 260 138 C160 143 70 150 0 170 Z" fill="var(--band-dark)"/>
      <path d="M0 170 C70 150 160 143 260 138 C380 132 470 80 560 66" fill="none" stroke="#ffe08a" stroke-width="2" opacity="0.7"/>
      <line x1="8" y1="52" x2="300" y2="52" stroke="var(--brand-orange)" stroke-width="1.5"/>
      <line x1="8" y1="100" x2="300" y2="100" stroke="var(--slogan-yellow)" stroke-width="1" opacity="0.6"/>
    </svg>
    <div class="brand">
      <span class="brand__mark"></span>
      <span class="brand__name">Tavrolen Goods</span>
    </div>
    <p class="slogan">Customize Your Lifestyle</p>
    <div class="person">
      <p class="person__name">Mirek Dunsby</p>
      <p class="person__role">Owner/Founder</p>
    </div>
    <div class="sofa-art" role="img" aria-label="Illustration of an ornate tufted vintage sofa"></div>
    <div class="footer-brand">
      <span class="footer-brand__mark"></span>
      <span class="footer-brand__name">TavrolenGoods</span>
    </div>
  </section>

  <section class="card card--back" aria-label="Card back">
    <svg class="card__wave" viewBox="0 0 560 358" aria-hidden="true">
      <path d="M0 0 H560 V66 C470 80 380 132 260 138 C160 143 70 150 0 170 Z" fill="var(--band-dark)"/>
      <path d="M0 170 C70 150 160 143 260 138 C380 132 470 80 560 66" fill="none" stroke="#ffe08a" stroke-width="2" opacity="0.7"/>
      <line x1="8" y1="52" x2="300" y2="52" stroke="var(--brand-orange)" stroke-width="1.5"/>
      <line x1="8" y1="100" x2="300" y2="100" stroke="var(--slogan-yellow)" stroke-width="1" opacity="0.6"/>
    </svg>
    <div class="brand">
      <span class="brand__mark"></span>
      <span class="brand__name">Tavrolen Goods</span>
    </div>
    <p class="slogan">Customize Your Lifestyle</p>
    <div class="contact-band"></div>
    <ul class="contact">
      <li><span class="contact__label">E-mail:</span>mdunsby@tavrolengoods.example</li>
      <li><span class="contact__label">Tel:</span>555-284-9173</li>
      <li>www.tavrolengoods.example</li>
    </ul>
    <div class="footer-brand">
      <span class="footer-brand__mark"></span>
      <span class="footer-brand__name">TavrolenGoods</span>
    </div>
  </section>

</main>
</body>
</html>
```